Stationary Design using supplied logo

24 Hour Completion required after acceptance

Business Cards
Letter Head
With Compliments Slips
Web Page Theme

Please only use a the following colors:

Red
Charcoal
Chrome/Silver
White

Red being the DOMINANT Color

Please email questions you may have.

Continued work available to suitably motivated designer.

Industry/Entity Type

Business

```html
<!DOCTYPE html>
<html lang="en">
<head>
<meta charset="utf-8">
<title>Business Card – Kindly Coin</title>
<link rel="stylesheet" href="https://fonts.googleapis.com/css2?family=Roboto+Slab:wght@400;600;700&display=swap">
<style>
  :root {
    --red: #d3281e;
    --charcoal: #2b3640;
    --silver: #dedede;
    --silver-light: #f3f3f3;
    --white: #ffffff;
    --page: #ffffff;
  }
  * { box-sizing: border-box; margin: 0; padding: 0; }
  html, body {
    width: 1200px;
    height: 1000px;
    overflow: hidden;
    background: var(--page);
  }
  .canvas {
    position: relative;
    width: 1200px;
    height: 1000px;
    font-family: "Roboto Slab", Georgia, serif;
  }
  .card {
    position: absolute;
    left: 390px;
    top: 160px;
    width: 420px;
    height: 680px;
    border: 1px solid #e6e6e6;
    overflow: hidden;
    text-align: center;
  }
  .card__pattern {
    position: absolute;
    inset: 0;
    background: linear-gradient(180deg, var(--silver-light) 0%, #eeeeee 50%, var(--silver-light) 100%);
  }
  .brand {
    position: absolute;
    left: 0;
    right: 0;
    top: 52px;
    display: flex;
    align-items: center;
    justify-content: center;
    gap: 14px;
  }
  .brand__dot {
    width: 30px;
    height: 30px;
    border-radius: 50%;
    background: var(--red);
  }
  .brand__name {
    font-size: 50px;
    font-weight: 400;
    color: var(--red);
    letter-spacing: 1px;
    line-height: 1;
  }
  .company {
    position: absolute;
    left: 0;
    right: 0;
    top: 216px;
    font-size: 33px;
    font-weight: 700;
    line-height: 42px;
    color: var(--red);
  }
  .name-band {
    position: absolute;
    left: 0;
    right: 0;
    top: 330px;
    height: 81px;
    background: var(--white);
    border-top: 1px solid var(--silver);
    border-bottom: 1px solid var(--silver);
    display: flex;
    align-items: center;
    justify-content: center;
  }
  .name-band__person {
    font-size: 28px;
    font-weight: 600;
    color: var(--charcoal);
  }
  .name-band__shadow {
    position: absolute;
    left: 40px;
    top: 411px;
    width: 340px;
    height: 24px;
  }
  .title {
    position: absolute;
    left: 0;
    right: 0;
    top: 438px;
    font-size: 18px;
    font-weight: 600;
    color: var(--red);
  }
  .contact {
    position: absolute;
    left: 0;
    right: 0;
    top: 533px;
    font-size: 19px;
    font-weight: 600;
    line-height: 24px;
    color: var(--charcoal);
    font-style: normal;
  }
</style>
</head>
<body>
<main class="canvas">
  <section class="card">
    <div class="card__pattern" role="img" aria-label="Soft silver diamond pattern background"></div>

    <div class="brand">
      <span class="brand__dot"></span>
      <span class="brand__name">Kindly Coin</span>
    </div>

    <h1 class="company">Comapny name's<br>here</h1>

    <div class="name-band">
      <h2 class="name-band__person">Person Name</h2>
    </div>
    <svg class="name-band__shadow" viewBox="0 0 340 24" aria-hidden="true">
      <defs>
        <radialGradient id="bandShadow" cx="50%" cy="0%" r="50%" gradientTransform="scale(1 0.5)">
          <stop offset="0%" stop-color="#000" stop-opacity="0.55"/>
          <stop offset="100%" stop-color="#000" stop-opacity="0"/>
        </radialGradient>
      </defs>
      <rect x="0" y="0" width="340" height="24" fill="url(#bandShadow)"/>
    </svg>

    <p class="title">Title</p>

    <address class="contact">
      Your Postal Address is here<br>
      Your contact number<br>
      abced124563@yourwebsite.com<br>
      www.yourwebsite.com
    </address>
  </section>
</main>
</body>
</html>
```